Velmora Home Page

I want to design a new home page using the look of two pages that I like.
http://us.tessandi.com/
http://www.morvane.us/?cm_mmc=seeker-_-EG_BR_Morvane_Exact_CAR_D-_-Search-_-morvanehttp://us.tessandi.com/
I like the framing of the tessandi site and the drop down feel of the morvane site. I will provide a new logo later today but for now can use what is already on my home page. The pictures in the middle of the page will rotate but I like the fonts and framing from Tessandi.
My current site is www.velmora.com and I had a designer do a file which came close but missed the mark attached. This upscale and elegant
I liek the top log but would want the glass tilted to look liek the rest of the letters and in a grey or silver elegant color.
High end individuals andn corporations

```html
<!DOCTYPE html>
<html lang="en">
<head>
<meta charset="utf-8">
<title>Velmora — Home</title>
<link rel="stylesheet" href="https://fonts.googleapis.com/css2?family=Lato:wght@300;400&display=swap">
<style>
  :root {
    --bar: #262626;
    --gold: #b08a4a;
    --gold-soft: #a9874f;
    --white: #ffffff;
    --band: rgba(20, 20, 20, 0.72);
    --rule: rgba(255, 255, 255, 0.75);
  }
  * { box-sizing: border-box; margin: 0; padding: 0; }
  html, body { width: 1200px; height: 967px; overflow: hidden; background: #111; }
  body { font-family: "Lato", Arial, sans-serif; color: var(--white); position: relative; }

  .site-header {
    position: absolute; left: 0; top: 0; width: 1200px; height: 115px;
    background: var(--bar); border-bottom: 3px solid var(--gold);
  }
  .brand {
    position: absolute; left: 152px; top: 26px;
    font-family: "Lato", Arial, sans-serif; font-weight: 300;
    font-size: 50px; letter-spacing: 1px; color: var(--white); line-height: 1;
  }
  .utility-nav {
    position: absolute; right: 148px; top: 19px;
    display: flex; align-items: center; gap: 9px;
    font-size: 10.5px; text-transform: uppercase; letter-spacing: 0.2px;
  }
  .utility-nav a { color: var(--white); text-decoration: none; }
  .utility-nav .sep { width: 1px; height: 8px; background: var(--white); }
  .utility-nav svg { display: block; }

  .main-nav {
    position: absolute; right: 148px; top: 84px;
    display: flex; gap: 18px; font-size: 14.5px; text-transform: uppercase;
  }
  .main-nav a { color: var(--white); text-decoration: none; }
  .main-nav a.current { color: var(--gold); }

  .hero-photo {
    position: absolute; left: 0; top: 115px; width: 1200px; height: 852px;
    background:
      radial-gradient(ellipse at 50% 30%, #9a9a9a 0%, #6b6b6b 30%, #3a3a3a 65%, #1a1a1a 100%);
  }
  .hero-band {
    position: absolute; left: 0; top: 423px; width: 1200px; height: 386px;
    background: var(--band); text-align: center;
  }
  .hero-band .band-brand {
    position: absolute; left: 0; width: 100%; top: 98px;
    font-weight: 300; font-size: 56px; letter-spacing: 1px; line-height: 1;
  }
  .hero-band .tagline {
    position: absolute; left: 0; width: 100%; top: 248px;
    font-weight: 300; font-size: 33px; letter-spacing: 0.5px; text-transform: uppercase; line-height: 1;
  }
  .hero-band .rule {
    position: absolute; left: 383px; top: 314px; width: 434px; height: 1px;
    background: linear-gradient(90deg, transparent, var(--rule) 15%, var(--rule) 85%, transparent);
  }
  .hero-band .discover {
    position: absolute; left: 0; width: 100%; top: 332px;
    font-size: 20px; letter-spacing: 1px; text-transform: uppercase;
    color: var(--gold); text-decoration: none;
  }

  .site-footer {
    position: absolute; left: 0; top: 846px; width: 1200px; height: 121px;
    background: rgba(22, 22, 22, 0.82); border-top: 3px solid var(--gold);
  }
  .copyright {
    position: absolute; left: 148px; top: 52px;
    font-size: 17px; color: var(--gold-soft); font-variant: small-caps;
  }
  .social { position: absolute; left: 950px; top: 47px; display: flex; gap: 6px; }
  .social span { width: 30px; height: 30px; background: #cfcfcf; display: block; }
</style>
</head>
<body>
  <header class="site-header">
    <div class="brand">Velmora</div>
    <nav class="utility-nav">
      <svg width="14" height="14" viewBox="0 0 14 14" aria-hidden="true"><circle cx="7" cy="4" r="3.5" fill="#fff"/><path d="M0 14c0-4 3-6 7-6s7 2 7 6z" fill="#fff"/></svg>
      <a href="#">Member Login</a><span class="sep"></span>
      <a href="#">Join Our Entourage</a><span class="sep"></span>
      <a href="#">Contact Us</a>
      <svg width="18" height="12" viewBox="0 0 18 12" aria-hidden="true"><rect x="0.5" y="0.5" width="17" height="11" fill="none" stroke="#fff"/><path d="M0.5 0.5L9 7l8.5-6.5" fill="none" stroke="#fff"/></svg>
    </nav>
    <nav class="main-nav">
      <a class="current" href="#">About Us</a>
      <a href="#">Entourage &amp; Staffing</a>
      <a href="#">Events</a>
      <a href="#">Travel</a>
      <a href="#">Celebrity &amp; PR</a>
      <a href="#">Other Services</a>
    </nav>
  </header>

  <div class="hero-photo" role="img" aria-label="Black and white photo of an elegant table setting with folded napkins, glassware and a mountain view through large windows"></div>

  <section class="hero-band">
    <div class="band-brand">Velmora</div>
    <h1 class="tagline">Access the best life has to offer</h1>
    <div class="rule"></div>
    <a class="discover" href="#">Discover More</a>
  </section>

  <footer class="site-footer">
    <p class="copyright">Copyright © 2014 Velmora, LLC</p>
    <div class="social" aria-label="Social links">
      <span></span><span></span><span></span>
    </div>
  </footer>
</body>
</html>
```